Courses Report - Analytics Redesign

We are a Learning Management System company that is looking to redesign our reporting suite in our product. We would like to add more graphs and visualizations to our reporting help communicate results and give our reporting a more modern look. Screenshots include our current courses report so that you can see the filters and type of data that our users search for. We are using Bramble Metrics as our reporting service and please see https://www.bramblemetrics.com/visual-gallery/ for examples of what type of visualizations can be generated.

Target Market(s)

LMS Administrators, Marketing and Sales Product Trainers

Number of Pages Required

1 page

Font styles to use
Sans Serif

Colors
33b8a4
33a6d7
0392cd
00a990
85cae6
87cfc6
cadf82
abd036
9bcb3b

Requirements
Must have
• Clean and simple look. Use Raleway as font. Easy to use and intuitive filtering. Ability to add/remove filters to the output. Graphical display of results that can drill down.
Nice to have
• Better way of listing other reports in menu on left.
Should not have
• Complicated graphs that cannot be easily understood.

```html
<!DOCTYPE html>
<html lang="en">
<head>
<meta charset="utf-8">
<title>Courses Report</title>
<link href="https://fonts.googleapis.com/css2?family=Open+Sans:wght@400;600;700&display=swap" rel="stylesheet">
<style>
:root{
  --sidebar:#0d3441;
  --active:#1f8fd3;
  --link:#33a6d7;
  --green:#8cc63f;
  --green-dark:#7ab730;
  --navy:#072a36;
  --sky:#29b3d6;
  --mint:#1dc08e;
  --page:#f4f5f6;
  --text:#333;
  --border:#b9bec2;
  --tag:#e4e6e8;
  --row-alt:#e9f3f9;
}
*{box-sizing:border-box;margin:0;padding:0}
html,body{width:816px;height:1200px;overflow:hidden}
body{font-family:"Open Sans",sans-serif;background:var(--page);color:var(--text);position:relative}
.sidebar{position:absolute;left:0;top:0;width:170px;height:1200px;background:var(--sidebar);color:#fff}
.brand{position:absolute;left:10px;top:22px;display:flex;align-items:center;gap:7px}
.brand-dot{width:30px;height:30px;border-radius:50%;background:var(--green)}
.brand-name{font-size:17px;font-weight:600;line-height:1.05}
.nav-item{position:absolute;left:0;width:170px;height:26px;display:flex;align-items:center;padding-left:16px;gap:10px;font-size:12px;font-weight:600}
.nav-item.active{background:var(--active);height:30px}
.nav-icon{width:14px;height:14px;fill:#fff}
.sub-item{position:absolute;left:56px;font-size:10px;color:#fff}
.sub-item.current{color:var(--link)}
.panel{position:absolute;left:197px;top:45px;width:543px;height:841px;background:#fff;box-shadow:0 0 4px rgba(0,0,0,.12)}
.label{position:absolute;right:435px;font-size:12px;font-weight:600;color:#333;text-align:right;white-space:nowrap}
.sublabel{position:absolute;right:345px;font-size:11px;color:#444;text-align:right;white-space:nowrap}
.sublabel.left{text-align:left;right:auto;left:132px;line-height:17px}
.field{position:absolute;left:125px;width:395px;height:32px;border:1px solid var(--border);display:flex;align-items:center;padding-left:4px;gap:4px;font-size:9.5px}
.field.plain{padding-left:10px}
.tag{background:var(--tag);border:1px solid #c9cccf;padding:4px 6px;font-size:9.5px;color:#444;white-space:nowrap}
.select{position:absolute;left:218px;width:302px;height:32px;border:1px solid var(--border);font-size:9.5px;display:flex;align-items:center;padding-left:10px}
.select::after{content:"";position:absolute;right:0;top:0;width:33px;height:30px;border-left:1px solid var(--border)}
.caret{position:absolute;right:12px;top:13px;border:4px solid transparent;border-top:5px solid #333}
.date{position:absolute;width:136px;height:32px;border:1px solid var(--border);font-size:9.5px;display:flex;align-items:center;padding-left:10px}
.check{position:absolute;font-size:10px;color:#555;display:flex;align-items:center;gap:6px;white-space:nowrap}
.box{width:9px;height:9px;border:1px solid #666;border-radius:1px;position:relative}
.box.on::after{content:"";position:absolute;left:2px;top:-1px;width:3px;height:6px;border:solid #555;border-width:0 1.5px 1.5px 0;transform:rotate(45deg)}
.btn{position:absolute;height:38px;border:2px solid var(--green);border-radius:19px;color:var(--green-dark);font-size:11px;font-weight:700;display:flex;align-items:center;justify-content:center}
.btn.solid{background:var(--green);color:#fff;border-color:var(--green)}
.chart{position:absolute;left:0;top:0}
.legend-row{position:absolute;left:255px;display:flex;align-items:center;font-size:12.5px;color:#222}
.swatch{width:30px;height:30px;margin-right:30px}
.legend-row b{margin-right:6px}
.report-table{position:absolute;left:198px;top:924px;width:541px;border-collapse:collapse;table-layout:fixed;font-size:9px;box-shadow:0 0 3px rgba(0,0,0,.15)}
.report-table th{background:var(--active);color:#fff;font-weight:600;font-size:10.5px;height:40px;border:1px solid #fff;line-height:1.2}
.report-table td{text-align:center;color:#555;border:1px solid #d8dcdf;background:#fff;line-height:1.45;padding:2px 0;white-space:nowrap;overflow:hidden}
.report-table tr:nth-child(odd) td{background:var(--row-alt)}
.footer{position:absolute;left:197px;width:543px;top:1162px;text-align:center;font-size:9.5px;color:#444}
</style>
</head>
<body>
<aside class="sidebar">
  <div class="brand"><span class="brand-dot"></span><span class="brand-name">Learnwise Hub</span></div>
  <div class="nav-item" style="top:84px"><svg class="nav-icon" viewBox="0 0 16 16"><path d="M8 1 0 8h2v7h4v-5h4v5h4V8h2z"/></svg>Home</div>
  <div class="nav-item" style="top:126px"><svg class="nav-icon" viewBox="0 0 16 16"><circle cx="8" cy="4" r="3"/><circle cx="3" cy="6" r="2"/><circle cx="13" cy="6" r="2"/><path d="M2 15c0-4 3-6 6-6s6 2 6 6z"/></svg>Users</div>
  <div class="nav-item active" style="top:166px"><svg class="nav-icon" viewBox="0 0 16 16"><path d="M1 1h1v13h13v1H1z"/><rect x="4" y="8" width="2" height="5"/><rect x="7" y="5" width="2" height="8"/><rect x="10" y="7" width="2" height="6"/><rect x="13" y="3" width="2" height="10"/></svg>Reports</div>
  <div class="sub-item" style="top:196px">Saved Reports</div>
  <div class="sub-item" style="top:217px">Users</div>
  <div class="sub-item current" style="top:238px">Courses</div>
  <div class="sub-item" style="top:259px">Due Dates</div>
  <div class="sub-item" style="top:280px">Classroom Enrollment</div>
  <div class="sub-item" style="top:301px">Course Survey</div>
  <div class="sub-item" style="top:322px">Satisfation Survey</div>
  <div class="sub-item" style="top:343px">Purchase History</div>
  <div class="nav-item" style="top:378px"><svg class="nav-icon" viewBox="0 0 16 16"><path d="M3 1h7l4 4v10H3z"/></svg>Content</div>
  <div class="nav-item" style="top:420px"><svg class="nav-icon" viewBox="0 0 16 16"><circle cx="8" cy="8" r="7"/></svg>Site</div>
</aside>

<section class="panel">
  <div class="label" style="top:39px">Groups</div>
  <div class="field" style="top:31px"><span class="tag">Sales&nbsp;&nbsp;X</span></div>
  <div class="label" style="top:85px">Course Sets</div>
  <div class="field" style="top:77px"><span class="tag">Course Type Examples&nbsp;&nbsp;X</span><span class="tag">ProLink Learning&nbsp;&nbsp;X</span><span class="tag">Sales Skills&nbsp;&nbsp;X</span></div>
  <div class="label" style="top:130px">Course Status</div>
  <div class="field plain" style="top:122px">Active Courses</div>
  <div class="label" style="top:176px">Courses</div>
  <div class="field" style="top:168px"><span class="tag">5 Management Mistakes Blocking Sales Reps from Selling&nbsp;&nbsp;X</span></div>
  <div class="label" style="top:221px">User Status</div>
  <div class="sublabel" style="top:222px">Training Status</div>
  <div class="select" style="top:213px">Complete<span class="caret"></span></div>
  <div class="sublabel" style="top:262px">User Status</div>
  <div class="select" style="top:253px">Active<span class="caret"></span></div>
  <div class="label" style="top:308px">Date Range</div>
  <div class="sublabel left" style="top:308px">Logged in On<br>Date Range</div>
  <div class="date" style="left:218px;top:300px">01/01/2019</div>
  <div class="sublabel" style="right:171px;top:309px">To</div>
  <div class="date" style="left:384px;top:300px">01/31/2019</div>
  <div class="check" style="left:133px;top:362px;font-weight:600;color:#333"><span class="box"></span>Select All</div>
  <div class="label" style="top:387px">Report Fields</div>
  <div class="check" style="left:133px;top:390px"><span class="box on"></span>Users: First Name</div>
  <div class="check" style="left:133px;top:413px"><span class="box on"></span>Users: Last Name</div>
  <div class="check" style="left:133px;top:437px"><span class="box on"></span>Users: Email Address</div>
  <div class="check" style="left:295px;top:390px"><span class="box on"></span>Courses: Course Name</div>
  <div class="check" style="left:295px;top:413px"><span class="box on"></span>Courses: User Status</div>
  <div class="check" style="left:295px;top:437px"><span class="box on"></span>Courses: Completion Date</div>
  <div class="check" style="left:295px;top:460px"><span class="box on"></span>Custom: Job Role</div>
  <div class="label" style="top:512px">Report Name</div>
  <div class="field" style="top:504px;width:272px"></div>
  <div class="btn solid" style="left:408px;top:501px;width:112px">SAVE REPORT</div>
  <div class="btn" style="left:125px;top:573px;width:82px">RESET</div>
  <div class="btn" style="left:217px;top:573px;width:129px">GENERATE REPORT</div>
  <div class="btn" style="left:356px;top:573px;width:129px">EXPORT TO EXCEL</div>

  <svg class="chart" width="543" height="841" viewBox="197 45 543 841" aria-label="Course status pie chart">
    <g stroke="#fff" stroke-width="2.5">
      <path d="M320 776L291.6 688.5A92 92 0 0 1 392.5 719.3Z" fill="var(--green)"/>
      <path d="M320 776L392.5 719.3A92 92 0 1 1 238 817.8Z" fill="var(--navy)"/>
      <path d="M320 776L238 817.8A92 92 0 0 1 228.1 772.8Z" fill="var(--mint)"/>
      <path d="M320 776L228.1 772.8A92 92 0 0 1 291.6 688.5Z" fill="var(--sky)"/>
    </g>
    <circle cx="320" cy="776" r="32" fill="#0a2430"/>
    <circle cx="320" cy="776" r="18" fill="#fff"/>
    <circle cx="320" cy="776" r="10" fill="var(--link)"/>
    <g fill="#fff" font-family="Open Sans, sans-serif" font-weight="700" font-size="12" text-anchor="middle">
      <text x="336" y="716">21%</text>
      <text x="272" y="745">28%</text>
      <text x="254" y="793">11%</text>
      <text x="350" y="826">60%</text>
    </g>
  </svg>
  <div class="legend-row" style="top:664px"><span class="swatch" style="background:var(--navy)"></span><b>60%</b>Course Completed</div>
  <div class="legend-row" style="top:700px"><span class="swatch" style="background:var(--green)"></span><b>21%</b>Course in Progress</div>
  <div class="legend-row" style="top:736px"><span class="swatch" style="background:var(--sky)"></span><b>28%</b>Top Learners</div>
  <div class="legend-row" style="top:772px"><span class="swatch" style="background:var(--mint)"></span><b>11%</b>Course not Started</div>
</section>

<table class="report-table">
  <colgroup><col style="width:54px"><col style="width:49px"><col style="width:106px"><col style="width:101px"><col style="width:78px"><col style="width:78px"><col style="width:75px"></colgroup>
  <tr><th>First<br>Name</th><th>Last<br>Name</th><th>Email Address</th><th>Course Name</th><th>User Status</th><th>Completion<br>Date</th><th>Job Role</th></tr>
  <tr style="height:38px"><td>Owen</td><td>Hartley</td><td>owenh@brightco.com</td><td>Determining<br>Customer Needs</td><td>Completed</td><td>04/21/2016</td><td>Manager</td></tr>
  <tr style="height:50px"><td>Owen</td><td>Hartley</td><td>owenh@brightco.com</td><td>5 Management<br>Mistakes Blocking Sales<br>reps from selling</td><td>Completed</td><td>04/21/2016</td><td>Manager</td></tr>
  <tr style="height:38px"><td>Owen</td><td>Hartley</td><td>owenh@brightco.com</td><td>PDF--The LMS<br>Evaluation Checklist</td><td>Completed</td><td>04/21/2016</td><td>Manager</td></tr>
  <tr style="height:37px"><td>Owen</td><td>Hartley</td><td>owenh@brightco.com</td><td>Health and Wellness</td><td>Completed</td><td>04/21/2016</td><td>Manager</td></tr>
</table>

<footer class="footer">Copyright © 2019, Learnwise Hub. All rights reserved.</footer>
</body>
</html>
```